Business card design only (Have Logo Online) Shoudl be quick and easy for designer

We would like to have a business card design that is in-line with our company logo. Final deliverables should include two EPS extension file. One for the front card design and the other the back-end design. Please also indicate the font style used.

Advisory Pebble is a social enterprise that focuses on utilizing technology, unique methodologies and international partnerships to provide a one-stop location for economical and dependable IT-related solutions.

Target Market(s)

Micro, small and medium business owners.

Industry/Entity Type

Business

Requirements
Must have
• The business card should incorporate our company logo.
Nice to have
• A little web 2.0 style would be nice but I haven''t decided yet.

```html
<!DOCTYPE html>
<html lang="en">
<head>
<meta charset="utf-8">
<title>Advisory Pebble — Business Card</title>
<link rel="stylesheet" href="https://fonts.googleapis.com/css2?family=Source+Sans+3:wght@400;700;800&family=Tangerine:wght@700&display=swap">
<style>
  :root {
    --card-green: #127a0a;
    --leaf-green: #43b02a;
    --pale-lime: #c6f28c;
    --text-white: #ffffff;
    --frame-black: #111111;
    --page-white: #ffffff;
  }
  * { box-sizing: border-box; margin: 0; padding: 0; }
  html, body {
    width: 1200px;
    height: 717px;
    overflow: hidden;
    background: var(--page-white);
  }
  .card {
    position: absolute;
    left: 0;
    top: 0;
    width: 1163px;
    height: 714px;
    background: var(--card-green);
    border: 3px solid var(--frame-black);
    overflow: hidden;
    font-family: "Source Sans 3", "Myriad Pro", Arial, sans-serif;
  }
  .brand {
    position: absolute;
    left: 66px;
    top: 176px;
    display: flex;
    align-items: center;
    gap: 14px;
  }
  .brand-dot {
    width: 40px;
    height: 40px;
    border-radius: 50%;
    background: var(--pale-lime);
  }
  .brand-name {
    font-weight: 800;
    font-size: 40px;
    letter-spacing: 2px;
    text-transform: uppercase;
    color: var(--leaf-green);
    line-height: 1;
  }
  .motif-area {
    position: absolute;
    left: 225px;
    top: 292px;
    width: 390px;
    height: 420px;
  }
  .details {
    position: absolute;
    right: 24px;
    top: 222px;
    text-align: right;
    color: var(--text-white);
  }
  .person-name {
    font-weight: 400;
    font-size: 41px;
    line-height: 1;
  }
  .tagline {
    margin-top: 10px;
    margin-right: -4px;
    font-family: "Tangerine", "Monotype Corsiva", cursive;
    font-weight: 700;
    font-size: 104px;
    line-height: 1;
    color: var(--pale-lime);
  }
  .contact {
    margin-top: 22px;
    list-style: none;
    font-size: 41px;
    line-height: 54px;
  }
</style>
</head>
<body>
  <main class="card">
    <div class="brand">
      <span class="brand-dot"></span>
      <span class="brand-name">Advisory Pebble</span>
    </div>

    <svg class="motif-area" viewBox="0 0 390 420" role="img" aria-label="Large decorative tree motif in light green">
      <defs>
        <radialGradient id="motifGlow" cx="50%" cy="45%" r="60%">
          <stop offset="0%" stop-color="#43b02a" stop-opacity="0.55"/>
          <stop offset="100%" stop-color="#43b02a" stop-opacity="0"/>
        </radialGradient>
      </defs>
      <rect width="390" height="420" fill="url(#motifGlow)"/>
    </svg>

    <section class="details">
      <p class="person-name">Darren Koh</p>
      <p class="tagline">‘Growing with you’</p>
      <ul class="contact">
        <li>2184 Alder Lane</li>
        <li>BC Canada</li>
        <li>V6M 2K3</li>
        <li>www.advisorypebble.com</li>
        <li>Cell: 1-604-555-0148</li>
      </ul>
    </section>
  </main>
</body>
</html>
```